Gold Harbor Concierge

I need a website developed for our travel concierge service. I'm looking to be able to collect information and have the information collected directed to a inbox. I would also like to me able to manage the updates to the website myself. I also would like a mobile version of the website to be included. Our services include assistance with Bachelor Parties, Bachelorette Parties and Medical Tourism. We provide custom packages that include Airport Transportation, Lodging, Bilingual guides and any other special needs identified by our clients.
Industry/Entity Type
Travel
Coding
Coded - Design and coding required
Number of Pages Required
4 page
Look and feel

```html
<!DOCTYPE html>
<html lang="en">
<head>
<meta charset="utf-8">
<title>Gold Harbor Concierge</title>
<link rel="stylesheet" href="https://fonts.googleapis.com/css2?family=Cinzel:wght@400;500&family=Nunito:wght@400;600&family=Montserrat:wght@500;600&family=Yellowtail&family=Playfair+Display&display=swap">
<style>
:root{
  --gold:#c8891a;
  --gold-soft:#e3c88f;
  --black:#000;
  --ink:#1a1a1a;
  --white:#fff;
  --footer:#0d0d0d;
}
*{box-sizing:border-box;margin:0;padding:0}
html,body{width:1200px;height:3967px;overflow:hidden}
body{position:relative;background:var(--white);font-family:"Nunito",sans-serif;color:var(--ink)}
.abs{position:absolute}
section,header,footer{position:absolute;left:0;width:1200px;overflow:hidden}
.heading{font-family:"Cinzel",serif;color:var(--gold);font-weight:400;letter-spacing:1px}
.swirl{display:block;width:26px;height:26px;border-radius:50%;border:2px solid var(--gold-soft)}

/* header + hero */
.site-header{top:0;height:62px;background:rgba(0,0,0,.82);z-index:3}
.brand-mark{left:159px;top:20px;font-family:"Cinzel",serif;color:var(--gold);font-size:15px;letter-spacing:.5px}
.social{top:22px;display:flex;gap:22px;left:893px}
.social span{width:10px;height:10px;border-radius:50%;background:var(--white)}
.menu-toggle{left:1008px;top:15px;width:32px;height:32px;border:1.5px solid var(--gold);border-radius:50%}
.menu-toggle i{position:absolute;left:9px;width:12px;height:1.5px;background:var(--white)}
.hero{top:0;height:533px}
.hero-photo{position:absolute;inset:0;background:radial-gradient(ellipse at 50% 35%,#8a5a48 0%,#4a2a26 45%,#1a0f10 100%)}
.hero-title{left:280px;width:640px;top:250px;text-align:center;font-family:"Yellowtail",cursive;font-weight:400;font-size:74px;line-height:80px;color:var(--white);white-space:nowrap}
.btn-outline{left:513px;top:354px;width:173px;height:50px;border:1px solid var(--gold);background:rgba(0,0,0,.55);color:var(--white);font-family:"Montserrat",sans-serif;font-size:15px;letter-spacing:1.5px;display:flex;align-items:center;justify-content:center}
.slide-nav{left:1024px;font-family:"Montserrat",sans-serif;font-size:14px;color:var(--white)}
.slide-nav.active{color:var(--gold)}

/* about */
.about{top:533px;height:593px}
.about h2{position:absolute;left:159px;top:122px;font-size:44px}
.about .swirl{position:absolute;left:159px;top:176px}
.about p{position:absolute;left:159px;top:208px;width:420px;font-size:16px;line-height:28.5px;color:#222}
.btn-solid{background:var(--black);color:var(--white);font-family:"Montserrat",sans-serif;font-size:16px;letter-spacing:1.5px;display:flex;align-items:center;justify-content:center}
.about .btn-solid{left:156px;top:351px;width:175px;height:54px}
.about-photo{left:590px;top:67px;width:578px;height:424px;background:radial-gradient(ellipse at 45% 50%,#a9a9a9 0%,#d4d4d4 45%,#fff 75%)}

/* services */
.services{top:1126px;height:582px;background:radial-gradient(ellipse at 50% 30%,#3a2630 0%,#1a1018 55%,#0e0a10 100%)}
.services h2{position:absolute;width:100%;text-align:center;top:65px;font-size:44px}
.services .swirl{position:absolute;left:587px;top:118px}
.service{position:absolute;top:190px;width:260px;text-align:center}
.service-photo{margin:0 auto;width:180px;height:180px;border-radius:50%;position:relative}
.service-photo::after{content:"";position:absolute;inset:-12px -14px -14px -12px;border-radius:50%;border:4px solid var(--gold);border-left-color:transparent;border-top-color:transparent;transform:rotate(20deg)}
.service h3{margin-top:26px;font-family:"Cinzel",serif;color:var(--gold);font-weight:400;font-size:19px}
.service p{margin-top:8px;font-size:12px;line-height:18px;color:var(--white)}
.service a{display:inline-block;margin-top:16px;font-family:"Montserrat",sans-serif;font-size:12px;letter-spacing:1.5px;color:var(--gold);text-decoration:underline}

/* packages */
.packages{top:1708px;height:714px;background:linear-gradient(180deg,#e8e8e8 0%,#f2f2f2 60%,#fff 100%)}
.packages h2{position:absolute;width:100%;text-align:center;top:70px;font-size:42px}
.packages .swirl{position:absolute;left:587px;top:126px}
.package{position:absolute;width:290px;height:290px}
.package svg{position:absolute;inset:0}
.package .txt{position:absolute;left:45px;width:200px;text-align:center}
.package h3{font-family:"Cinzel",serif;font-weight:400;font-size:20px;line-height:25px;color:#222}
.package p{margin-top:8px;font-size:16px;line-height:22px;color:#333}

/* newsletter */
.newsletter{top:2422px;height:451px}
.newsletter-photo{position:absolute;left:0;top:0;width:1200px;height:320px;background:linear-gradient(90deg,#4a3a30,#7a6a5c 40%,#5c4a40 70%,#3a3030)}
.newsletter-box{left:234px;top:181px;width:732px;height:270px;background:var(--black);text-align:center}
.newsletter-box h2{margin-top:32px;font-size:42px}
.newsletter-box .swirl{margin:8px auto 0}
.newsletter-box p{margin-top:10px;font-size:16px;color:#ccc}
.email-field{left:185px;top:166px;width:368px;height:51px;background:var(--white);font-family:"Playfair Display",serif;font-size:18px;color:#222;display:flex;align-items:center;justify-content:center}
.email-field svg{position:absolute;right:14px;top:16px}

/* contact form */
.contact{top:2873px;height:493px}
.contact-photo{left:662px;top:0;width:538px;height:493px;background:radial-gradient(ellipse at 55% 45%,#e9dcae 0%,#f3ebd3 45%,#fff 80%)}
.contact h2{position:absolute;left:159px;top:34px;font-size:42px}
.contact .swirl{position:absolute;left:159px;top:88px}
.field{position:absolute;border:1px solid #bbb;background:var(--white);font-size:15px;color:#444;padding:8px 10px}
.contact .btn-solid{left:159px;top:345px;width:174px;height:54px}

/* info strip */
.info{top:3366px;height:228px;background:#141414}
.info-col{position:absolute;top:80px;width:300px;text-align:center}
.info-col h4{font-family:"Playfair Display",serif;font-weight:400;color:var(--gold);font-size:15px;letter-spacing:.5px}
.info-col p{margin-top:16px;font-size:13px;line-height:20px;letter-spacing:1px;color:#ddd}
.divider{top:61px;width:1px;height:128px;background:#444}

/* footer */
.site-footer{top:3594px;height:373px;background:var(--footer);text-align:center}
.footer-brand{position:absolute;width:100%;top:36px;font-family:"Cinzel",serif;color:var(--gold);font-size:24px;line-height:30px}
.footer-brand span{display:block;width:38px;height:38px;margin:0 auto 6px;border-radius:50%;border:2px solid var(--gold)}
.site-footer p{position:absolute;left:420px;width:360px;top:124px;font-family:"Playfair Display",serif;font-size:12px;line-height:22px;color:#ddd}
.footer-nav{position:absolute;width:100%;top:273px;display:flex;justify-content:center;gap:18px;align-items:center;font-family:"Montserrat",sans-serif;font-size:10px;color:var(--gold);letter-spacing:1px}
.footer-nav i{width:4px;height:4px;border-radius:50%;background:var(--gold)}
.copyright{position:absolute;left:0;bottom:0;width:100%;height:45px;background:var(--gold);color:#fff;font-size:9px;display:flex;align-items:center;justify-content:center}
</style>
</head>
<body>

<header class="site-header">
  <div class="abs brand-mark">Gold Harbor</div>
  <div class="abs social"><span></span><span></span><span></span></div>
  <div class="abs menu-toggle"><i style="top:11px"></i><i style="top:15px"></i><i style="top:19px"></i></div>
</header>

<section class="hero">
  <div class="hero-photo" role="img" aria-label="Photo of friends celebrating with cocktails"></div>
  <h1 class="abs hero-title">Travel Concierge Service</h1>
  <div class="abs btn-outline">CONTACT US</div>
  <svg class="abs" style="left:571px;top:457px" width="60" height="60" viewBox="0 0 60 60"><path d="M30 2 58 30 30 58 2 30Z" fill="none" stroke="#c8891a" stroke-width="1.5"/><path d="M20 27 30 36 40 27" fill="none" stroke="#c8891a" stroke-width="2"/></svg>
  <div class="abs slide-nav active" style="top:228px">01</div>
  <div class="abs" style="left:1078px;top:236px;width:122px;height:1px;background:#c8891a"></div>
  <div class="abs slide-nav" style="top:264px">02</div>
  <div class="abs slide-nav" style="top:298px">03</div>
</section>

<section class="about">
  <h2 class="heading">About Us</h2>
  <span class="swirl"></span>
  <p>Lorem ipsum dolor sit amet, consectetur adipielit, sed do eiusmod tempor incididunt ut labore et dolore magna aliqua. Quis ipsum suspendisse ultrices gravida. Risus commodo viverra maecenas vel facilisis.</p>
  <div class="abs btn-solid">READ MORE</div>
  <div class="abs about-photo" role="img" aria-label="Black and white photo of friends toasting with champagne"></div>
</section>

<section class="services">
  <h2 class="heading">Our Services</h2>
  <span class="swirl"></span>
  <div class="service" style="left:144px">
    <div class="service-photo" role="img" aria-label="Photo of friends toasting with beer at a bar" style="background:radial-gradient(circle,#a06a50,#4a2a40)"></div>
    <h3>Bachelor Parties</h3>
    <p>Lorem ipsum dolor sit amet, coctetur<br>adipielit, sed do eiusm</p>
    <a>READ MORE</a>
  </div>
  <div class="service" style="left:474px">
    <div class="service-photo" role="img" aria-label="Photo of a bachelorette party with decorations" style="background:radial-gradient(circle,#f0d8e0,#c8a0b0)"></div>
    <h3>Bachelorette Parties</h3>
    <p>Lorem ipsum dolor sit amet, coctetur<br>adipielit, sed do eiusm</p>
    <a>READ MORE</a>
  </div>
  <div class="service" style="left:805px">
    <div class="service-photo" role="img" aria-label="Photo of a traveller with luggage at an airport" style="background:radial-gradient(circle,#c0ccd6,#6a7a88)"></div>
    <h3>Medical Tourism</h3>
    <p>Lorem ipsum dolor sit amet, coctetur<br>adipielit, sed do eiusm</p>
    <a>READ MORE</a>
  </div>
</section>

<section class="packages">
  <h2 class="heading">Custom Packages</h2>
  <span class="swirl"></span>

  <div class="package" style="left:160px;top:178px">
    <svg viewBox="0 0 290 290"><path d="M145 2 288 145 145 288 2 145Z" fill="rgba(255,255,255,.35)" stroke="#c8891a" stroke-width="1.5"/><path d="M145 2 212 69H78Z" fill="#c8891a"/><path d="M110 255H180L145 288Z" fill="#000"/><path d="M120 56H170M145 44V64M132 52 158 52" stroke="#fff" stroke-width="3"/><path d="M137 270H153M148 265 153 270 148 275" stroke="#c8891a" stroke-width="1.5" fill="none"/></svg>
    <div class="txt" style="top:94px"><h3>Airport<br>Transportation</h3><p>suspendisse ultces grda Risus commodo maecenas</p></div>
  </div>
  <div class="package" style="left:456px;top:178px">
    <svg viewBox="0 0 290 290"><path d="M145 2 288 145 145 288 2 145Z" fill="rgba(255,255,255,.35)" stroke="#c8891a" stroke-width="1.5"/><path d="M145 2 212 69H78Z" fill="#c8891a"/><path d="M110 255H180L145 288Z" fill="#000"/><rect x="130" y="40" width="30" height="24" fill="#fff"/><path d="M137 270H153M148 265 153 270 148 275" stroke="#c8891a" stroke-width="1.5" fill="none"/></svg>
    <div class="txt" style="top:106px"><h3>Lodging</h3><p>suspendisse ultces grda Risus commodo maecenas</p></div>
  </div>
  <div class="package" style="left:752px;top:178px">
    <svg viewBox="0 0 290 290"><path d="M145 2 288 145 145 288 2 145Z" fill="rgba(255,255,255,.35)" stroke="#c8891a" stroke-width="1.5"/><path d="M145 2 212 69H78Z" fill="#c8891a"/><path d="M110 255H180L145 288Z" fill="#000"/><circle cx="145" cy="46" r="6" fill="#fff"/><path d="M133 64Q145 50 157 64Z" fill="#fff"/><path d="M137 270H153M148 265 153 270 148 275" stroke="#c8891a" stroke-width="1.5" fill="none"/></svg>
    <div class="txt" style="top:94px"><h3>Bilingual<br>Guides</h3><p>suspendisse ultces grda Risus commodo maecenas</p></div>
  </div>
  <div class="package" style="left:308px;top:340px">
    <svg viewBox="0 0 290 290"><path d="M145 2 288 145 145 288 2 145Z" fill="rgba(255,255,255,.6)" stroke="#c8891a" stroke-width="1.5"/><path d="M145 2 212 69H78Z" fill="#c8891a"/><path d="M110 255H180L145 288Z" fill="#000"/><path d="M133 62 145 40 157 62Z" fill="none" stroke="#fff" stroke-width="2.5"/><path d="M137 270H153M148 265 153 270 148 275" stroke="#c8891a" stroke-width="1.5" fill="none"/></svg>
    <div class="txt" style="top:108px"><h3>Special Needs</h3><p>suspendisse ultces grda Risus commodo maecenas</p></div>
  </div>
  <div class="package" style="left:605px;top:340px">
    <svg viewBox="0 0 290 290"><path d="M145 2 288 145 145 288 2 145Z" fill="rgba(255,255,255,.6)" stroke="#c8891a" stroke-width="1.5"/><path d="M145 2 212 69H78Z" fill="#c8891a"/><path d="M110 255H180L145 288Z" fill="#000"/><rect x="136" y="40" width="18" height="24" fill="#fff"/><path d="M137 270H153M148 265 153 270 148 275" stroke="#c8891a" stroke-width="1.5" fill="none"/></svg>
    <div class="txt" style="top:96px"><h3>And Many<br>More</h3><p>suspendisse ultces grda Risus commodo maecenas</p></div>
  </div>
</section>

<section class="newsletter">
  <div class="newsletter-photo" role="img" aria-label="Blurred photo of friends dining together"></div>
  <div class="abs newsletter-box">
    <h2 class="heading">Stay In Touch</h2>
    <span class="swirl"></span>
    <p>Signup to recieve news and updates from Gold Harbor Concierge</p>
    <div class="abs email-field">Enter your e-mail
      <svg width="20" height="20" viewBox="0 0 20 20"><path d="M2 10 18 2 13 18 9 11Z" fill="none" stroke="#c8891a" stroke-width="1.5"/></svg>
    </div>
  </div>
</section>

<section class="contact">
  <div class="abs contact-photo" role="img" aria-label="Photo of champagne glasses"></div>
  <h2 class="heading">Get In Touch</h2>
  <span class="swirl"></span>
  <div class="field" style="left:159px;top:126px;width:238px;height:40px">Name</div>
  <div class="field" style="left:404px;top:126px;width:237px;height:40px">Email</div>
  <div class="field" style="left:159px;top:174px;width:238px;height:41px">Phone</div>
  <div class="field" style="left:404px;top:174px;width:237px;height:41px">Subject</div>
  <div class="field" style="left:159px;top:223px;width:482px;height:111px">Your Message</div>
  <div class="abs btn-solid">SEND NOW</div>
</section>

<section class="info">
  <div class="info-col" style="left:106px"><h4>LOCATION</h4><p>12 Harbour Lane,<br>Port Vale, Westmere</p></div>
  <div class="abs divider" style="left:433px"></div>
  <div class="info-col" style="left:450px"><h4>PHONE</h4><p>01 555 010 234<br>00 555 010 876</p></div>
  <div class="abs divider" style="left:758px"></div>
  <div class="info-col" style="left:784px"><h4>EMAIL</h4><p>info@goldharborconcierge.com</p></div>
</section>

<footer class="site-footer">
  <div class="footer-brand"><span></span>Gold Harbor</div>
  <p>Lorem ipsum dolor sit amet, consectetur adipiscing elit, sed do eiusmor incididunt ut labore et dolore magna aliqua. Quis ipsum suspendisse ultrices grada. Risus commodo viverra maecenas aclacus vel facilisis.</p>
  <nav class="footer-nav"><span>HOME</span><i></i><span>ABOUT US</span><i></i><span>SERVICES</span><i></i><span>CONTACT</span></nav>
  <div class="copyright">© 2021 Gold Harbor Concierge. All right reserved.</div>
</footer>

</body>
</html>
```